Small Business Consulting Firm Needs Business Card Design

Need a sleek modern business card with 2 sides matching the colors of our logo. We will be placing these with a mailer we are sending out. These business cards will only ever be given to business owners. We operate helping businesses who are struggling with cash flow or finances. If the green and blue design needs to be moved to the right of "Harborline Crest Consulting" for aesthetic purposes that is ok. We will need an editable file if possible. We would like to include the reps name, email, website, and phone number. For now just use Peter Vance, pvance@harborlinecrest.com, www.harborlinecrest.com, and 833-555-0172.

```html
<!DOCTYPE html>
<html lang="en">
<head>
<meta charset="UTF-8">
<title>Harborline Crest Consulting — Business Card</title>
<link href="https://fonts.googleapis.com/css2?family=Lato:wght@400;700&display=swap" rel="stylesheet">
<style>
  :root {
    --stage: #2b2d30;
    --card-dark: #3a3b3d;
    --card-light: #ffffff;
    --brand-green: #6cb33f;
    --brand-blue: #1e88d0;
    --text-light: #f2f2f2;
    --text-muted: #d6d6d6;
    --text-dark: #3a3b3d;
  }
  * { margin: 0; padding: 0; box-sizing: border-box; }
  html, body {
    width: 1200px; height: 900px; overflow: hidden;
    background: var(--stage);
    font-family: "Lato", Arial, sans-serif;
  }
  .card {
    position: absolute;
    border-radius: 22px;
    overflow: hidden;
    box-shadow: 0 12px 30px rgba(0,0,0,0.45);
  }
  /* Front: vertical card */
  .card-front {
    left: 110px; top: 150px;
    width: 340px; height: 595px;
    background: var(--card-light);
  }
  .card-front .swoosh { position: absolute; inset: 0; width: 100%; height: 100%; }
  .rep {
    position: absolute; right: 30px; top: 36px;
    text-align: right; color: var(--text-light);
  }
  .rep-name { font-size: 30px; font-weight: 700; letter-spacing: 1px; line-height: 1.1; }
  .rep-position { font-size: 15px; color: var(--brand-green); margin-top: 2px; }
  .rep-rule {
    display: block; width: 150px; height: 3px; margin: 8px 0 0 auto;
    background: linear-gradient(to right, var(--text-light) 0 78%, var(--brand-blue) 78% 100%);
  }
  .contact-list {
    position: absolute; left: 28px; top: 150px;
    list-style: none; color: var(--text-muted); font-size: 14px;
  }
  .contact-list li { display: flex; align-items: center; gap: 10px; margin-bottom: 12px; }
  .contact-list svg { width: 14px; height: 14px; flex: none; }
  .brand {
    position: absolute; display: flex; align-items: center; gap: 14px;
  }
  .brand-mark { width: 26px; height: 26px; background: var(--brand-green); flex: none; }
  .brand-name {
    font-size: 17px; font-weight: 400; letter-spacing: 3px;
    text-transform: uppercase; line-height: 1.35;
  }
  .card-front .brand { left: 50%; top: 470px; transform: translateX(-50%); width: 270px; }
  .card-front .brand-name { color: var(--text-dark); }
  /* Back: horizontal card */
  .card-back {
    left: 510px; top: 280px;
    width: 595px; height: 340px;
    background: var(--card-dark);
  }
  .card-back .brand { left: 50%; top: 50%; transform: translate(-50%, -50%); width: 340px; }
  .card-back .brand-name { color: var(--text-light); font-size: 20px; }
</style>
</head>
<body>
  <section class="card card-front">
    <svg class="swoosh" viewBox="0 0 340 595" preserveAspectRatio="none" aria-hidden="true">
      <path d="M0,0 H340 V150 C305,320 165,395 0,410 Z" fill="var(--brand-blue)"/>
      <path d="M0,0 H340 V122 C305,292 165,366 0,382 Z" fill="var(--brand-green)"/>
      <path d="M0,0 H340 V95 C305,262 165,336 0,352 Z" fill="var(--card-dark)"/>
    </svg>
    <div class="rep">
      <div class="rep-name">PETER VANCE</div>
      <div class="rep-position">Position</div>
      <span class="rep-rule"></span>
    </div>
    <ul class="contact-list">
      <li>
        <svg viewBox="0 0 24 24"><path fill="var(--brand-green)" d="M6.6 10.8a15 15 0 0 0 6.6 6.6l2.2-2.2c.3-.3.7-.4 1-.2 1.1.4 2.300.6 3.6.6.6 0 1 .4 1 1V20c0 .6-.4 1-1 1A17 17 0 0 1 3 4c0-.6.4-1 1-1h3.5c.6 0 1 .4 1 1 0 1.3.2 2.5.6 3.600.1.3 0 .7-.2 1z"/></svg>
        <span>833-555-0172</span>
      </li>
      <li>
        <svg viewBox="0 0 24 24"><path fill="var(--brand-green)" d="M2 5h20v14H2z"/><path fill="none" stroke="var(--card-dark)" stroke-width="2" d="M2 5l10 8 10-8"/></svg>
        <span>pvance@harborlinecrest.com</span>
      </li>
      <li>
        <svg viewBox="0 0 24 24"><circle cx="12" cy="12" r="10" fill="none" stroke="var(--brand-green)" stroke-width="2"/><path fill="none" stroke="var(--brand-green)" stroke-width="1.6" d="M2 12h20M12 2c3 3 3 17 0 20M12 2c-3 3-3 17 0 20"/></svg>
        <span>www.harborlinecrest.com</span>
      </li>
    </ul>
    <div class="brand">
      <span class="brand-mark"></span>
      <span class="brand-name">Harborline Crest Consulting</span>
    </div>
  </section>

  <section class="card card-back">
    <div class="brand">
      <span class="brand-mark"></span>
      <span class="brand-name">Harborline Crest Consulting</span>
    </div>
  </section>
</body>
</html>
```